VENTIX Business Card

VENTIX (www.ventixpools.example) is a veteran in the swimming pool maintenance and repair business..we have served our clients for 15 years and have a research chemist, an electrician, a plumber and a pool building contractor (in part) on staff...We want to provide a business card that has a dual purpose, that people want to keep around, that leaves people speechless in the sense that they understand the mission of and the experience level of the TEAM at VENTIX.

Target Market(s)

persons who enjoy swimming and make it a priority to swim

Industry/Entity Type

Building

Font styles to use
Serif
Sans Serif

Colors
85acd3
3176b5
95b6d8
3276b5
0355a3
0555a3
0255a3
0455a3
85abd2

Requirements
Must have
• name, title, address, email, text
Nice to have
• a die cut shape
Should not have
• cartoons, pictures of pools

```html
<!DOCTYPE html>
<html lang="en">
<head>
<meta charset="utf-8">
<title>VENTIX Business Card</title>
<link rel="stylesheet" href="https://fonts.googleapis.com/css2?family=Open+Sans:wght@400;600&family=Josefin+Sans:wght@300;400&display=swap">
<style>
  :root {
    --blue-deep: #0255a3;
    --blue-mid: #3176b5;
    --blue-soft: #85acd3;
    --blue-pale: #95b6d8;
    --ink: #222;
    --paper: #ffffff;
    --backdrop: #e9edf2;
  }
  * { margin: 0; padding: 0; box-sizing: border-box; }
  html, body { width: 1200px; height: 1037px; overflow: hidden; }
  body {
    background: var(--backdrop);
    font-family: "Open Sans", Arial, sans-serif;
    position: relative;
  }
  .card {
    position: absolute;
    left: 190px;
    width: 820px;
    height: 469px;
    border-radius: 4px;
    overflow: hidden;
    box-shadow: 0 10px 30px rgba(0, 0, 0, 0.25);
  }
  /* Back side */
  .card-back {
    top: 36px;
    background: radial-gradient(ellipse at 40% 45%, var(--blue-mid) 0%, var(--blue-deep) 75%);
    color: var(--paper);
  }
  .card-back .gloss {
    position: absolute;
    top: 0; bottom: 0; left: 520px; width: 140px;
    background: linear-gradient(90deg, rgba(255,255,255,0) 0%, rgba(255,255,255,0.14) 50%, rgba(255,255,255,0) 100%);
  }
  .back-brand {
    position: absolute;
    top: 170px; left: 0; right: 0;
    text-align: center;
  }
  .back-brand .brand-name {
    font-family: "Josefin Sans", "Open Sans", sans-serif;
    font-weight: 400;
    font-size: 52px;
    letter-spacing: 6px;
    color: var(--paper);
  }
  .back-brand .site {
    margin-top: 18px;
    font-size: 17px;
    letter-spacing: 3px;
  }
  /* Front side */
  .card-front {
    top: 532px;
    background: var(--paper);
    color: var(--ink);
  }
  .front-panel { position: absolute; inset: 0; }
  .contact {
    position: absolute;
    left: 0; top: 70px; width: 440px;
    text-align: center;
  }
  .contact .brand-name {
    font-family: "Josefin Sans", "Open Sans", sans-serif;
    font-weight: 400;
    font-size: 34px;
    letter-spacing: 5px;
    color: var(--blue-mid);
  }
  .contact .person {
    margin-top: 26px;
    font-size: 25px;
    font-weight: 400;
  }
  .contact .role { font-size: 15px; color: #444; margin-top: 2px; }
  .details {
    margin-top: 18px;
    font-size: 18px;
    line-height: 27px;
  }
  .details dt { display: inline; font-weight: 600; }
  .details dd { display: inline; }
  .details .row { display: block; }
  .address { margin-top: 18px; font-size: 17px; }
  .front-brand {
    position: absolute;
    left: 500px; right: 0; top: 195px;
    text-align: center;
    color: var(--paper);
  }
  .front-brand .brand-name {
    font-family: "Josefin Sans", "Open Sans", sans-serif;
    font-weight: 400;
    font-size: 64px;
    letter-spacing: 6px;
    line-height: 1;
  }
  .front-brand .tagline {
    margin-top: 14px;
    font-family: "Josefin Sans", "Open Sans", sans-serif;
    font-weight: 300;
    font-size: 16px;
    letter-spacing: 2.5px;
    white-space: nowrap;
  }
</style>
</head>
<body>

<section class="card card-back">
  <div class="gloss"></div>
  <div class="back-brand">
    <div class="brand-name">VENTIX</div>
    <div class="site">www.ventixpools.example</div>
  </div>
</section>

<section class="card card-front">
  <svg class="front-panel" width="820" height="469" viewBox="0 0 820 469" aria-hidden="true">
    <defs>
      <linearGradient id="panelFill" x1="0" y1="0" x2="1" y2="0">
        <stop offset="0" stop-color="#0355a3"/>
        <stop offset="0.35" stop-color="#0555a3"/>
        <stop offset="0.55" stop-color="#3176b5"/>
        <stop offset="1" stop-color="#85acd3"/>
      </linearGradient>
      <linearGradient id="panelGloss" x1="0" y1="0" x2="1" y2="0">
        <stop offset="0" stop-color="#fff" stop-opacity="0"/>
        <stop offset="0.5" stop-color="#fff" stop-opacity="0.18"/>
        <stop offset="1" stop-color="#fff" stop-opacity="0"/>
      </linearGradient>
    </defs>
    <path d="M520 0 Q 380 200 452 469 L820 469 L820 0 Z" fill="url(#panelFill)"/>
    <rect x="540" y="0" width="130" height="469" fill="url(#panelGloss)"/>
  </svg>

  <div class="contact">
    <div class="brand-name">VENTIX</div>
    <div class="person">Youre Name</div>
    <div class="role">Director</div>
    <dl class="details">
      <span class="row"><dt>Phone:</dt> <dd>+(000) 1234 5678</dd></span>
      <span class="row"><dt>Mail:</dt><dd>admin@ventixpools.example</dd></span>
      <span class="row"><dt>Website:</dt> <dd>www.ventixpools.example</dd></span>
    </dl>
    <div class="address">480 Harbor Lane, Bayview 54321</div>
  </div>

  <div class="front-brand">
    <div class="brand-name">VENTIX</div>
    <div class="tagline">POOL CARE...PERFECTED</div>
  </div>
</section>

</body>
</html>
```